Vodka label designing in name of brand name KORVANE

We need a label design for VODKA.Name of brand is KORVANE.
Targeted consumers are are young males and females.
Product will be in different 7 flavours.
Product will be triple distilled and silver filtered very rich and premium quality product.
I have to keep same theme for different flavours of vodka.
only colour and image of fruit will change.
As the name suggest its KORVANE its liberty to drink and be happy.
Label Design must be very rich,simple,attractive and unforgettable just like inside product.

Target Market(s)

YOUTH males and females, bar tenders,mixers, universal product

Industry/Entity Type

Product

Requirements
Must have
• rich look and easy to remember.
Nice to have
• any connection with WORD KORVANE
Should not have
• ANYTHING RELATED TO KORVANE FIGNTING

```html
<!DOCTYPE html>
<html lang="en">
<head>
<meta charset="utf-8">
<title>KORVANE Premium Vodka – Label</title>
<link rel="stylesheet" href="https://fonts.googleapis.com/css2?family=Oswald:wght@500;600;700&family=Cinzel:wght@400&family=Great+Vibes&display=swap">
<style>
  :root {
    --page: #f6f1e7;
    --red: #b3121b;
    --red-dark: #7d0c12;
    --silver: #c9ccd1;
    --silver-dark: #8d9298;
    --white: #ffffff;
    --gold: #c9a24a;
    --ink: #1d1a18;
    --green: #8cc63f;
    --green-dark: #5f9a22;
  }
  html, body {
    margin: 0;
    padding: 0;
    width: 815px;
    height: 1200px;
    overflow: hidden;
    background: var(--page);
  }
  .canvas {
    position: relative;
    width: 815px;
    height: 1200px;
  }
  .label {
    position: absolute;
    left: 67px;
    top: 95px;
    width: 680px;
    height: 1010px;
  }
  .brand-name { font-family: "Oswald", sans-serif; font-weight: 700; fill: var(--white); letter-spacing: 4px; }
  .premium { font-family: "Cinzel", serif; fill: var(--gold); letter-spacing: 10px; }
  .product { font-family: "Oswald", sans-serif; font-weight: 700; fill: var(--red); letter-spacing: 2px; }
  .claim { font-family: "Great Vibes", cursive; fill: var(--ink); }
  .flavour { font-family: "Oswald", sans-serif; font-weight: 600; fill: var(--white); letter-spacing: 1px; }
  .volume { font-family: "Oswald", sans-serif; font-weight: 600; fill: var(--white); letter-spacing: 2px; }
  .strength { font-family: "Oswald", sans-serif; font-weight: 500; fill: var(--ink); }
</style>
</head>
<body>
<div class="canvas">
  <svg class="label" viewBox="0 0 680 1010" xmlns="http://www.w3.org/2000/svg">
    <g class="label-body">
      <path d="M60 170 H620 V300 L650 330 V720 L620 750 V900 Q470 960 340 1000 Q210 960 60 900 V750 L30 720 V330 L60 300 Z"
            fill="var(--silver)" />
      <path d="M72 180 H608 V305 L636 333 V716 L608 744 V892 Q465 948 340 986 Q215 948 72 892 V744 L44 716 V333 L72 305 Z"
            fill="var(--red)" />
      <path d="M86 190 H594 V312 L620 338 V710 L594 736 V882 Q460 934 340 970 Q220 934 86 882 V736 L60 710 V338 L86 312 Z"
            fill="var(--white)" />
      <path d="M79 186 H601 V309 L628 336 V713 L601 740 V887 Q462 941 340 978 Q218 941 79 887 V740 L52 713 V336 L79 309 Z"
            fill="none" stroke="var(--white)" stroke-width="2" stroke-dasharray="2 5" />
    </g>

    <g class="brand-banner">
      <path d="M70 10 Q210 40 340 40 Q470 40 610 10 Q680 10 680 105 Q680 200 610 200 Q470 170 340 170 Q210 170 70 200 Q0 200 0 105 Q0 10 70 10 Z"
            fill="var(--silver)" />
      <path d="M72 22 Q210 52 340 52 Q470 52 608 22 Q666 24 666 105 Q666 186 608 188 Q470 158 340 158 Q210 158 72 188 Q14 186 14 105 Q14 24 72 22 Z"
            fill="var(--red)" />
      <text class="brand-name" x="340" y="140" text-anchor="middle" font-size="112">KORVANE</text>
    </g>

    <text class="premium" x="340" y="255" text-anchor="middle" font-size="34">PREMIUM</text>
    <text class="product" x="340" y="360" text-anchor="middle" font-size="118">VODKA</text>

    <g class="flourishes">
      <rect role="img" aria-label="Gold ornamental flourish, left" x="115" y="425" width="140" height="8" rx="4" fill="var(--gold)" opacity="0.45" />
      <rect role="img" aria-label="Gold ornamental flourish, right" x="425" y="425" width="140" height="8" rx="4" fill="var(--gold)" opacity="0.45" />
    </g>

    <text class="claim" x="340" y="455" text-anchor="middle" font-size="60">Triple</text>
    <text class="claim" x="340" y="525" text-anchor="middle" font-size="60">Distilled<tspan font-size="30">and</tspan></text>
    <text class="claim" x="340" y="600" text-anchor="middle" font-size="60">Silver Filtered</text>

    <g class="flavour-ribbon">
      <path d="M0 690 L260 660 V790 L20 820 L45 752 Z" fill="var(--green-dark)" />
      <path d="M680 690 L420 660 V790 L660 820 L635 752 Z" fill="var(--green-dark)" />
      <path d="M40 705 L300 675 V800 L40 830 Z" fill="var(--green)" stroke="var(--silver)" stroke-width="5" />
      <path d="M640 705 L380 675 V800 L640 830 Z" fill="var(--green)" stroke="var(--silver)" stroke-width="5" />
      <text class="flavour" x="160" y="782" text-anchor="middle" font-size="50" transform="rotate(-7 160 765)">ORANGE</text>
      <text class="flavour" x="520" y="782" text-anchor="middle" font-size="50" transform="rotate(7 520 765)">FLAVOR</text>
      <circle role="img" aria-label="Illustration of green apples" cx="340" cy="740" r="85" fill="var(--green)" />
    </g>

    <rect class="volume-tab" x="245" y="835" width="190" height="46" fill="var(--red)" stroke="var(--silver)" stroke-width="4" />
    <text class="volume" x="340" y="869" text-anchor="middle" font-size="28">750 ML.</text>

    <text class="strength" x="340" y="922" text-anchor="middle" font-size="22">ALC. 50% VOL</text>
  </svg>
</div>
</body>
</html>
```